People/Expertise finder to associate people to experts, services and products

Design a mock-up for a Kinward Atlas/expertise finder system. The people/expertise finder project is targeting to relate people to experts, countries and core operations. We are expecting the final UI to be responsive. The styleguide that is followed in the enterprise is attached for reference. further documents outlining the vision is also attached. Based on queries kindly use the tovel net profile as an example of profile page. People will search using the enterprise search on names, skills etc to find matching people.

Kinward Atlas

3 page

• The UI should be aesthetically good and should bring in the industry standards

```html
<!DOCTYPE html>
<html lang="en">
<head>
<meta charset="utf-8">
<title>Kinward Atlas – Search Results</title>
<link href="https://fonts.googleapis.com/css2?family=Open+Sans:wght@400;600;700&family=Roboto:wght@400;500&display=swap" rel="stylesheet">
<style>
:root{
  --navy:#0e2545;
  --navy-line:#3c5373;
  --blue:#1472d8;
  --social:#1a86c8;
  --page:#ececec;
  --white:#ffffff;
  --ink:#1b1b1b;
  --muted:#7a7a7a;
  --line:#e6e6e6;
  --gold:#f5b400;
  --field:#d6d6d6;
}
*{box-sizing:border-box;margin:0;padding:0}
html,body{width:1011px;height:1200px;overflow:hidden}
body{background:var(--page);font-family:"Roboto",Arial,sans-serif;color:var(--ink);position:relative}

.topbar{position:absolute;left:0;top:0;width:1011px;height:44px;background:var(--navy);border-bottom:2px solid var(--navy-line)}
.brand{position:absolute;left:122px;top:9px;display:flex;align-items:center;gap:8px;color:var(--white);font-size:12.5px;font-weight:500;letter-spacing:.3px}
.brand-dot{width:26px;height:26px;border-radius:50%;border:2px solid var(--white)}
.top-icon{position:absolute;top:15px}
.badge{position:absolute;top:-4px;right:-6px;width:10px;height:10px;border-radius:50%;background:var(--blue);color:var(--white);font-size:7px;line-height:10px;text-align:center}
.user{position:absolute;left:786px;top:9px;display:flex;align-items:center;gap:8px;color:var(--white);font-size:11px}
.user-photo{width:26px;height:26px;border-radius:50%;background:radial-gradient(circle at 50% 40%,#e8c7a8,#8a6048)}

.search-field{position:absolute;left:121px;top:65px;width:451px;height:34px;background:var(--white);font-size:11.5px;padding:10px 12px;color:#444}
.search-btn{position:absolute;left:582px;top:65px;width:111px;height:34px;background:var(--blue);color:var(--white);font-size:10px;font-weight:500;display:flex;align-items:center;justify-content:center;gap:7px;letter-spacing:.3px}
.count{position:absolute;left:121px;top:110px;font-size:9.5px}
.count b{font-weight:500}

.results{position:absolute;left:121px;top:134px;width:572px;height:1032px;background:var(--white)}
.tabs{display:flex;height:35px;border-bottom:1px solid var(--line)}
.tab{font-size:8.8px;padding:0 13px;line-height:35px;border-right:1px solid var(--line);color:#333}
.tab.active{border-bottom:3px solid var(--navy)}
.person{position:relative;height:121.5px;border-bottom:1px solid var(--line)}
.avatar{position:absolute;left:21px;top:21px;width:45px;height:45px;border-radius:50%;background:radial-gradient(circle at 50% 40%,#9a9a9a,#3e3e3e 70%,#cfcfcf)}
.name{position:absolute;left:87px;top:19px;font-family:"Open Sans",sans-serif;font-weight:700;font-size:10px;color:#333;display:flex;align-items:center;gap:9px}
.gold{background:var(--gold);color:var(--white);font-size:5px;padding:1px 4px;border-radius:1px;letter-spacing:.5px}
.role{position:absolute;left:87px;top:35px;font-family:"Open Sans",sans-serif;font-size:7px;color:var(--muted)}
.divider{position:absolute;left:87px;right:21px;top:52px;border-top:1px solid var(--line)}
.social{position:absolute;left:87px;top:59px;display:flex;gap:12px;font-family:"Roboto",sans-serif;font-weight:500;font-size:7.5px;color:var(--social)}
.profile-btn{position:absolute;left:472px;top:20px;width:80px;height:18px;border:1px solid var(--blue);border-radius:2px;color:var(--blue);font-size:7.8px;text-align:center;line-height:16px;letter-spacing:.3px}
.field{position:absolute;top:80px}
.field .label{font-family:"Open Sans",sans-serif;font-size:5.5px;font-weight:700;letter-spacing:.6px;color:#777}
.field .value{font-size:7.5px;margin-top:4px}
.f-phone{left:21px}.f-email{left:198px}.f-address{left:394px}

.filter{position:absolute;left:714px;top:65px;width:176px;height:303px;background:var(--white)}
.filter h2{font-size:9px;font-weight:500;height:35px;line-height:35px;padding-left:13px;border-bottom:1px solid var(--line)}
.filter-label{position:absolute;left:13px;font-size:8px;font-weight:400;color:#222}
.filter-input{position:absolute;left:13px;width:150px;height:21px;border:1px solid var(--field);font-size:8px;color:#555;padding:0 6px;line-height:19px}
.caret{position:absolute;right:8px;top:8px;width:0;height:0;border-left:4px solid transparent;border-right:4px solid transparent;border-top:4px solid #aaa}
.filter-apply{position:absolute;left:14px;top:237px;width:149px;height:27px;background:var(--blue);color:var(--white);font-size:9.5px;text-align:center;line-height:27px}
</style>
</head>
<body>

<header class="topbar">
  <div class="brand"><span class="brand-dot"></span>Kinward Atlas</div>
  <div class="top-icon" style="left:707px">
    <svg width="14" height="11" viewBox="0 0 14 11"><rect x="0.5" y="0.5" width="13" height="10" rx="1" fill="#fff"/><path d="M1 1.5 7 6 13 1.5" stroke="#0e2545" stroke-width="1.2" fill="none"/></svg>
    <span class="badge">1</span>
  </div>
  <div class="top-icon" style="left:737px;top:14px">
    <svg width="12" height="13" viewBox="0 0 12 13"><path d="M6 1C3.5 1 2.5 3 2.5 5v3L1 10h10L9.5 8V5C9.5 3 8.5 1 6 1z" fill="#fff"/><circle cx="6" cy="11.5" r="1.3" fill="#fff"/></svg>
    <span class="badge">4</span>
  </div>
  <div class="user">
    <span class="user-photo" role="img" aria-label="Signed-in user photo"></span>
    <span>Hello Olden</span>
    <svg width="9" height="6" viewBox="0 0 9 6"><path d="M1 1l3.5 3.5L8 1" stroke="#fff" stroke-width="1.8" fill="none"/></svg>
  </div>
</header>

<div class="search-field">Olden</div>
<div class="search-btn">
  <svg width="15" height="15" viewBox="0 0 15 15"><circle cx="6.5" cy="6.5" r="5" stroke="#fff" stroke-width="1.8" fill="none"/><path d="M10 10l3.5 3.5" stroke="#fff" stroke-width="2"/></svg>
  SEARCH
</div>
<div class="count"><b>292,816 results -</b> people for Olden</div>

<main class="results">
  <nav class="tabs">
    <span class="tab active">People</span><span class="tab">Country</span><span class="tab">Program</span><span class="tab">Most Reviewed</span><span class="tab">Most Popular</span>
  </nav>

  <article class="person"><span class="avatar" role="img" aria-label="Profile photo of Ravi Olden"></span><div class="name">RAVI OLDEN <span class="gold">GOLD</span></div><div class="role">Sales &amp; Marketing</div><div class="profile-btn">VIEW PROFILE</div><div class="divider"></div><div class="social"><span>tovel net</span><span>Plazo</span><span>Chirra</span></div><div class="field f-phone"><div class="label">PHONE</div><div class="value">(+31) 555 019 274</div></div><div class="field f-email"><div class="label">EMAIL</div><div class="value">raviolden@mailbay.com</div></div><div class="field f-address"><div class="label">ADDRESS</div><div class="value">Lindenhof 12, Vessford</div></div></article>
  <article class="person"><span class="avatar" role="img" aria-label="Profile photo of Ravi Olden"></span><div class="name">RAVI OLDEN <span class="gold">GOLD</span></div><div class="role">Sales &amp; Marketing</div><div class="profile-btn">VIEW PROFILE</div><div class="divider"></div><div class="social"><span>tovel net</span><span>Plazo</span><span>Chirra</span></div><div class="field f-phone"><div class="label">PHONE</div><div class="value">(+31) 555 019 274</div></div><div class="field f-email"><div class="label">EMAIL</div><div class="value">raviolden@mailbay.com</div></div><div class="field f-address"><div class="label">ADDRESS</div><div class="value">Lindenhof 12, Vessford</div></div></article>
  <article class="person"><span class="avatar" role="img" aria-label="Profile photo of Ravi Olden"></span><div class="name">RAVI OLDEN <span class="gold">GOLD</span></div><div class="role">Sales &amp; Marketing</div><div class="profile-btn">VIEW PROFILE</div><div class="divider"></div><div class="social"><span>tovel net</span><span>Plazo</span><span>Chirra</span></div><div class="field f-phone"><div class="label">PHONE</div><div class="value">(+31) 555 019 274</div></div><div class="field f-email"><div class="label">EMAIL</div><div class="value">raviolden@mailbay.com</div></div><div class="field f-address"><div class="label">ADDRESS</div><div class="value">Lindenhof 12, Vessford</div></div></article>
  <article class="person"><span class="avatar" role="img" aria-label="Profile photo of Ravi Olden"></span><div class="name">RAVI OLDEN <span class="gold">GOLD</span></div><div class="role">Sales &amp; Marketing</div><div class="profile-btn">VIEW PROFILE</div><div class="divider"></div><div class="social"><span>tovel net</span><span>Plazo</span><span>Chirra</span></div><div class="field f-phone"><div class="label">PHONE</div><div class="value">(+31) 555 019 274</div></div><div class="field f-email"><div class="label">EMAIL</div><div class="value">raviolden@mailbay.com</div></div><div class="field f-address"><div class="label">ADDRESS</div><div class="value">Lindenhof 12, Vessford</div></div></article>
  <article class="person"><span class="avatar" role="img" aria-label="Profile photo of Ravi Olden"></span><div class="name">RAVI OLDEN <span class="gold">GOLD</span></div><div class="role">Sales &amp; Marketing</div><div class="profile-btn">VIEW PROFILE</div><div class="divider"></div><div class="social"><span>tovel net</span><span>Plazo</span><span>Chirra</span></div><div class="field f-phone"><div class="label">PHONE</div><div class="value">(+31) 555 019 274</div></div><div class="field f-email"><div class="label">EMAIL</div><div class="value">raviolden@mailbay.com</div></div><div class="field f-address"><div class="label">ADDRESS</div><div class="value">Lindenhof 12, Vessford</div></div></article>
  <article class="person"><span class="avatar" role="img" aria-label="Profile photo of Ravi Olden"></span><div class="name">RAVI OLDEN <span class="gold">GOLD</span></div><div class="role">Sales &amp; Marketing</div><div class="profile-btn">VIEW PROFILE</div><div class="divider"></div><div class="social"><span>tovel net</span><span>Plazo</span><span>Chirra</span></div><div class="field f-phone"><div class="label">PHONE</div><div class="value">(+31) 555 019 274</div></div><div class="field f-email"><div class="label">EMAIL</div><div class="value">raviolden@mailbay.com</div></div><div class="field f-address"><div class="label">ADDRESS</div><div class="value">Lindenhof 12, Vessford</div></div></article>
  <article class="person"><span class="avatar" role="img" aria-label="Profile photo of Ravi Olden"></span><div class="name">RAVI OLDEN <span class="gold">GOLD</span></div><div class="role">Sales &amp; Marketing</div><div class="profile-btn">VIEW PROFILE</div><div class="divider"></div><div class="social"><span>tovel net</span><span>Plazo</span><span>Chirra</span></div><div class="field f-phone"><div class="label">PHONE</div><div class="value">(+31) 555 019 274</div></div><div class="field f-email"><div class="label">EMAIL</div><div class="value">raviolden@mailbay.com</div></div><div class="field f-address"><div class="label">ADDRESS</div><div class="value">Lindenhof 12, Vessford</div></div></article>
  <article class="person"><span class="avatar" role="img" aria-label="Profile photo of Ravi Olden"></span><div class="name">RAVI OLDEN <span class="gold">GOLD</span></div><div class="role">Sales &amp; Marketing</div><div class="profile-btn">VIEW PROFILE</div><div class="divider"></div><div class="social"><span>tovel net</span><span>Plazo</span><span>Chirra</span></div><div class="field f-phone"><div class="label">PHONE</div><div class="value">(+31) 555 019 274</div></div><div class="field f-email"><div class="label">EMAIL</div><div class="value">raviolden@mailbay.com</div></div><div class="field f-address"><div class="label">ADDRESS</div><div class="value">Lindenhof 12, Vessford</div></div></article>
</main>

<aside class="filter">
  <h2>FILTER SEARCH RESULTS</h2>
  <span class="filter-label" style="top:47px">COUNTRY</span>
  <div class="filter-input" style="top:61px">United States<span class="caret"></span></div>
  <span class="filter-label" style="top:94px">SKILLS</span>
  <div class="filter-input" style="top:108px"></div>
  <span class="filter-label" style="top:141px">PROFESSIONS</span>
  <div class="filter-input" style="top:155px"></div>
  <span class="filter-label" style="top:188px">WORKING EXPERIENCE</span>
  <div class="filter-input" style="top:202px">&gt; 1 year<span class="caret"></span></div>
  <div class="filter-apply">SEARCH</div>
</aside>

</body>
</html>
```